Business card for event manager / organizer "velmora tandem"

Draft of a new valuable business card for my company.
Events, personnel service providers, festivals

```html
<!DOCTYPE html>
<html lang="de">
<head>
<meta charset="utf-8">
<title>velmora tandem – Visitenkarte</title>
<link rel="stylesheet" href="https://fonts.googleapis.com/css2?family=Anton&family=Rajdhani:wght@300&display=swap">
<style>
  :root {
    --card-black: #191818;
    --hex-black: #161515;
    --accent-orange: #ef7d1a;
    --text-white: #ffffff;
    --tagline-grey: #cfcfcf;
  }
  html, body {
    margin: 0;
    padding: 0;
    width: 1200px;
    height: 720px;
    overflow: hidden;
    background: var(--card-black);
  }
  .card {
    position: relative;
    width: 1200px;
    height: 720px;
    background: var(--card-black);
    overflow: hidden;
  }
  .card-backdrop {
    position: absolute;
    inset: 0;
  }
  .brand-square {
    position: absolute;
    left: 676px;
    top: 302px;
    width: 106px;
    height: 106px;
    background: var(--accent-orange);
  }
  .brand-name {
    position: absolute;
    left: 807px;
    top: 326px;
    margin: 0;
    font-family: "Anton", "Impact", sans-serif;
    font-weight: 400;
    font-size: 38px;
    line-height: 44px;
    letter-spacing: 1px;
    text-transform: uppercase;
    color: var(--text-white);
    white-space: nowrap;
  }
  .brand-tagline {
    position: absolute;
    left: 757px;
    top: 420px;
    width: 264px;
    margin: 0;
    font-family: "Rajdhani", "Arial", sans-serif;
    font-weight: 300;
    font-size: 15px;
    line-height: 18px;
    color: var(--tagline-grey);
    white-space: nowrap;
  }
</style>
</head>
<body>
  <div class="card">
    <svg class="card-backdrop" width="1200" height="720" viewBox="0 0 1200 720" aria-hidden="true">
      <defs>
        <filter id="hex-shadow" x="-20%" y="-20%" width="140%" height="140%">
          <feDropShadow dx="-36" dy="-8" stdDeviation="12" flood-color="#000" flood-opacity="0.85"/>
        </filter>
      </defs>
      <polygon class="accent-field" points="698,0 1200,0 1200,720 698,720 905,360" fill="var(--accent-orange)"/>
      <polygon class="feature-hexagon" points="851,41 1128,201 1128,519 851,679 576,519 576,201"
               fill="var(--hex-black)" filter="url(#hex-shadow)"/>
    </svg>

    <div class="brand-square"></div>
    <h1 class="brand-name">velmora<br>tandem</h1>
    <p class="brand-tagline">...denn jedes Fest verdient guten Service!</p>
  </div>
</body>
</html>
```